Deactivated Coal-Fired Power Plant to be redeveloped into a Green Energy Campus.

Want a striking business card statement that introduces our concept project to provide economic and community recovery to a former rural coal community in western PA.
Essentially 12 project representatives that will lead both the demolition of an existing power plant and the redevelopment to a new Green energy site.
Business Card should reflect our effort.
We are open to ideas.

Target Market(s)

Energy and Power Generation industries

Industry/Entity Type

Power Generation and Data Centers

Contact Information for Business Card

Included in uploaded materials

Font styles to use
Sans Serif
Other font styles liked:
• Arial, Calibri

Requirements
Must have
• Multiple colors

```html
<!DOCTYPE html>
<html lang="en">
<head>
<meta charset="UTF-8">
<title>Ridgeline Renewal – Business Card</title>
<link href="https://fonts.googleapis.com/css2?family=Montserrat:wght@400;500;800&display=swap" rel="stylesheet">
<style>
  :root {
    --green: #0f9a44;
    --ink: #111111;
    --card-dark: #1c1c1c;
    --card-light: #ffffff;
    --paper: #e9e9e9;
    --white: #ffffff;
  }
  * { box-sizing: border-box; margin: 0; padding: 0; }
  html, body { width: 1200px; height: 1200px; overflow: hidden; }
  body {
    background: var(--paper);
    font-family: "Montserrat", Arial, sans-serif;
    display: flex;
    align-items: center;
    justify-content: center;
    gap: 80px;
  }
  .card {
    width: 400px;
    height: 700px;
    border-radius: 28px;
    position: relative;
    overflow: hidden;
    box-shadow: 0 8px 24px rgba(0,0,0,0.18);
  }
  .brand {
    display: flex;
    flex-direction: column;
    align-items: center;
    gap: 18px;
  }
  .brand-mark {
    width: 130px;
    height: 130px;
    border-radius: 50%;
    background: var(--green);
  }
  .brand-name {
    font-weight: 800;
    font-size: 30px;
    letter-spacing: 1px;
    text-transform: uppercase;
    text-align: center;
    line-height: 1.1;
  }

  /* Front */
  .card-front { background: var(--card-dark); color: var(--white); }
  .card-front .brand { position: absolute; top: 140px; left: 0; right: 0; }
  .card-front .brand-name { color: var(--white); }
  .contact-block { position: absolute; left: 70px; top: 440px; }
  .contact-name {
    color: var(--green);
    font-weight: 500;
    font-size: 38px;
    letter-spacing: -1px;
    line-height: 1;
  }
  .contact-title { font-size: 22px; font-weight: 400; margin-top: 6px; letter-spacing: -0.5px; }
  .contact-list { list-style: none; margin-top: 18px; }
  .contact-list li {
    display: flex; align-items: center; gap: 12px;
    font-size: 22px; font-weight: 400; line-height: 1.55;
  }
  .contact-list svg { width: 24px; height: 24px; flex: none; }

  /* Back */
  .card-back { background: var(--card-light); color: var(--ink); }
  .card-back .brand { position: absolute; top: 80px; left: 0; right: 0; }
  .card-back .brand-name { color: var(--ink); }
  .statement { position: absolute; top: 330px; left: 30px; right: 30px; text-align: center; }
  .statement-heading {
    color: var(--green); font-weight: 500; font-size: 30px; margin-bottom: 12px;
  }
  .statement-body { font-weight: 800; font-size: 19px; line-height: 1.45; }
  .accent-band {
    position: absolute; left: 0; right: 0; bottom: 0; height: 16px; background: var(--green);
  }
</style>
</head>
<body>
  <section class="card card-front">
    <div class="brand">
      <div class="brand-mark"></div>
      <div class="brand-name">Ridgeline<br>Renewal</div>
    </div>
    <div class="contact-block">
      <div class="contact-name">FULL NAME</div>
      <div class="contact-title">TITLE</div>
      <ul class="contact-list">
        <li>
          <svg viewBox="0 0 24 24" aria-hidden="true"><path fill="#0f9a44" d="M6.6 10.8a15 15 0 0 0 6.6 6.6l2.2-2.2a1 1 0 0 1 1-.25 11.4 11.4 0 0 0 3.6.57 1 1 0 0 1 1 1V20a1 1 0 0 1-1 1A17 17 0 0 1 3 4a1 1 0 0 1 1-1h3.5a1 1 0 0 1 1 1c0 1.25.2 2.45.57 3.57a1 1 0 0 1-.25 1z"/></svg>
          (000) 000 0000
        </li>
        <li>
          <svg viewBox="0 0 24 24" aria-hidden="true"><rect x="6" y="2" width="12" height="20" rx="2" fill="none" stroke="#0f9a44" stroke-width="2"/><circle cx="12" cy="18" r="1.2" fill="#0f9a44"/></svg>
          (000) 000 0000
        </li>
        <li>
          <svg viewBox="0 0 24 24" aria-hidden="true"><rect x="2" y="5" width="20" height="14" fill="#0f9a44"/><path d="M2 5l10 8 10-8" fill="none" stroke="#1c1c1c" stroke-width="1.6"/></svg>
          email@company.com
        </li>
      </ul>
    </div>
  </section>

  <section class="card card-back">
    <div class="brand">
      <div class="brand-mark"></div>
      <div class="brand-name">Ridgeline<br>Renewal</div>
    </div>
    <div class="statement">
      <h2 class="statement-heading">STATEMENT</h2>
      <p class="statement-body">Lorem ipsum dolor sit amet conse tetuer adipiscing elit, sed diam nonummy nibh euismod tincidunt ut laoreet dolore magna aliquam erat sed diam nonummy nibh euismod tincidunt ut laoreet dolore magna aliquam erat</p>
    </div>
    <div class="accent-band"></div>
  </section>
</body>
</html>
```